Packaging Design for a Bakery Shop

We are opening a Bakery Shop in the Kingdom of Bahrain where we are going to sell bread items, Cakes, sweets, etc..and we have already selected the name and the logo design (check file named Crumvella to see the logo) .

We are looking to obtain designs for our packaging mainly the following (to see the plain sample items to be used for designing see the attached files with the same names):

1. Cake Box.
2. Pastry Box.
3. Brown bakery bags.
4. White bakery bags.
5. White nylon bags.
6. Toast transparent nylon bag.
7. Coffee paper cup.
8. Napkin.
9. Stickers (this should be a sticker to be used for packaging items that can not be printable so we can use the stickers instead).

Note that priority is for the cake box and the others can have the similar theme. So for designing the above, you are kindly requested to use a base similar to the attached files not other cuts. The designer may start his submission by applying the design on the cake box.

The theme to be designed by the designer should take into consideration the fact that the colours to be used shall be matching for sweets and breads. Also as you can see in the attached logo design it is kind of mid to high product price so the theme shall match with this level.

Also the designer shall bear in mind that we want a packaging design that is easy to apply and cost effective. Maximum colours to be used for packaging should be 3 colours only.

Note that the logo colour is still not defined, so you need also to change the logo colour to make it matching with the packaging.

Regards
Tariq Habbal
+973 36512248

Target Market(s)

It is mainly women since they are the one going mainly for the bakeries. Customers are mainly walking in customers.

Industry/Entity Type

Bakery

Font styles to use
Decorative

Requirements
Must have
• The design should be unique having a new idea and not same as others.
• The design should be cost effective and can be applied in all packaging in the bakery.
• In the design we need to have some part for the instgram, tweeter, phone icons.
• It should be suitable for both bread items and sweet items.
Should not have
• No more than 3 colours design

```html
<!DOCTYPE html>
<html lang="en">
<head>
<meta charset="utf-8">
<title>Crumvella Packaging</title>
<link href="https://fonts.googleapis.com/css2?family=Allura&family=Montserrat:wght@400;500&display=swap" rel="stylesheet">
<style>
  :root{
    --bg:#f3f3f4;
    --teal:#137f74;
    --mint:#8fd1b3;
    --cream:#f7efc2;
    --cream-light:#fdfbe9;
    --kraft:#c79a6a;
    --kraft-edge:#a57c50;
    --butter:#f1e6a8;
    --dieline:#c9c9c9;
    --cut-line:#b9ddd2;
    --label:#555;
    --leader:#777;
  }
  html,body{margin:0;padding:0;overflow:hidden;}
  body{width:1200px;height:1000px;background:var(--bg);}
  .sheet{display:block;width:1200px;height:1000px;}
  .brand-name{font-family:"Allura",cursive;fill:var(--teal);}
  .tagline{font-family:"Montserrat",sans-serif;font-size:9px;letter-spacing:1.6px;fill:var(--teal);}
  .contact{font-family:"Montserrat",sans-serif;font-size:7px;fill:var(--teal);}
  .bag-contact-text{font-family:"Montserrat",sans-serif;font-size:5.5px;fill:var(--teal);}
  .sticker-text{font-family:"Montserrat",sans-serif;font-size:9px;letter-spacing:1.5px;fill:var(--teal);}
  .bag-seal-text{font-family:"Montserrat",sans-serif;font-size:5px;letter-spacing:1px;fill:var(--teal);}
  .caption{font-family:"Montserrat",sans-serif;font-size:14px;fill:var(--label);}
</style>
</head>
<body>
<svg class="sheet" viewBox="0 0 1200 1000" xmlns="http://www.w3.org/2000/svg">
  <defs>
    <radialGradient id="panelGlow" cx="0.6" cy="0.55" r="0.6">
      <stop offset="0" stop-color="#fffdf2"/>
      <stop offset="1" stop-color="#f5eab8"/>
    </radialGradient>
    <linearGradient id="wheatTone" x1="0" y1="1" x2="1" y2="0">
      <stop offset="0" stop-color="#a86d1c"/>
      <stop offset="0.5" stop-color="#d9a441"/>
      <stop offset="1" stop-color="#f5e7b0" stop-opacity="0"/>
    </linearGradient>
  </defs>

  <g class="box-dieline">
    <!-- top flaps -->
    <path class="top-flap" d="M145 215 V88 H493 V215 Z" fill="var(--cream)"/>
    <path class="top-flap" d="M493 215 V107 H617 V215 Z" fill="var(--cream)"/>
    <rect class="top-band" x="145" y="88" width="485" height="19" fill="var(--teal)"/>
    <path class="top-flap" d="M948 215 V100 H1087 V215 Z" fill="var(--cream)"/>
    <path class="tuck-line" d="M160 88 V60 Q160 52 168 52 H478 Q486 52 486 60 V88" fill="none" stroke="var(--dieline)"/>
    <path class="tuck-line" d="M500 107 V125 L505 135 V215 M610 107 V125 L605 135 V215" fill="none" stroke="var(--dieline)"/>
    <path class="tuck-line" d="M960 215 V130 L965 120 V100 M1075 100 V120 L1080 130 V215" fill="none" stroke="var(--dieline)"/>

    <!-- glue flap -->
    <path class="glue-flap" d="M145 215 L117 240 V445 L145 470 Z" fill="var(--cream-light)" stroke="var(--dieline)"/>

    <!-- walls -->
    <rect class="wall front" x="145" y="213" width="348" height="257" fill="url(#panelGlow)"/>
    <rect class="wall side" x="493" y="213" width="124" height="257" fill="url(#panelGlow)"/>
    <rect class="wall back" x="617" y="213" width="343" height="257" fill="url(#panelGlow)"/>
    <rect class="wall side" x="960" y="213" width="127" height="257" fill="url(#panelGlow)"/>
    <path class="fold-lines" d="M493 213 V470 M617 213 V470 M960 213 V470 M145 213 H1087" stroke="var(--dieline)" fill="none"/>

    <!-- wheat artwork areas -->
    <rect role="img" aria-label="Golden wheat ears illustration" x="148" y="250" width="190" height="218" fill="url(#wheatTone)"/>
    <rect role="img" aria-label="Golden wheat ears illustration" x="620" y="250" width="190" height="218" fill="url(#wheatTone)"/>

    <!-- front brand lockup -->
    <text class="brand-name" x="385" y="352" font-size="40" text-anchor="middle">Crumvella</text>
    <text class="tagline" x="385" y="374" text-anchor="middle">LOAVES, TREATS &amp; BEYOND</text>
    <!-- back brand lockup -->
    <text class="brand-name" x="870" y="352" font-size="40" text-anchor="middle">Crumvella</text>
    <text class="tagline" x="870" y="374" text-anchor="middle">LOAVES, TREATS &amp; BEYOND</text>

    <!-- certificate badges -->
    <rect class="badge" x="578" y="222" width="26" height="26" fill="#fff"/>
    <rect class="badge" x="1050" y="222" width="26" height="26" fill="#fff"/>

    <!-- side contact strip -->
    <g class="contact-strip" transform="translate(606 462) rotate(-90)">
      <circle cx="4" cy="-3" r="4" fill="var(--teal)"/>
      <text class="contact" x="12" y="0">+973 36512248</text>
      <circle cx="74" cy="-3" r="4" fill="var(--teal)"/>
      <text class="contact" x="82" y="0">@crumvella</text>
      <circle cx="130" cy="-3" r="4" fill="var(--teal)"/>
      <text class="contact" x="138" y="0">@crumvella</text>
      <circle cx="186" cy="-3" r="4" fill="var(--teal)"/>
    </g>

    <!-- colour strip -->
    <g class="colour-strip">
      <rect x="145" y="466" width="942" height="9" fill="var(--cream)"/>
      <rect x="192" y="466" width="50" height="9" fill="var(--teal)"/>
      <rect x="242" y="466" width="100" height="9" fill="var(--mint)"/>
      <rect x="342" y="466" width="50" height="9" fill="var(--teal)"/>
      <rect x="442" y="466" width="51" height="9" fill="var(--mint)"/>
      <rect x="541" y="466" width="50" height="9" fill="var(--teal)"/>
      <rect x="591" y="466" width="26" height="9" fill="var(--mint)"/>
      <rect x="690" y="466" width="50" height="9" fill="var(--teal)"/>
      <rect x="790" y="466" width="50" height="9" fill="var(--teal)"/>
      <rect x="890" y="466" width="50" height="9" fill="var(--mint)"/>
      <rect x="990" y="466" width="50" height="9" fill="var(--teal)"/>
      <rect x="1040" y="466" width="47" height="9" fill="var(--mint)"/>
    </g>

    <!-- bottom flaps -->
    <g class="bottom-flaps" fill="var(--teal)">
      <path role="img" aria-label="Teal panel with bakery doodle pattern" d="M145 475 H493 V620 H408 L378 565 H268 L238 620 H145 Z"/>
      <path role="img" aria-label="Teal panel with bakery doodle pattern" d="M493 475 H617 V492 L560 560 H512 V522 H493 Z"/>
      <path role="img" aria-label="Teal panel with bakery doodle pattern" d="M617 475 H960 V620 H878 L848 565 H738 L708 620 H617 Z"/>
      <path role="img" aria-label="Teal panel with bakery doodle pattern" d="M960 475 H1087 V495 L1030 560 H978 V520 H960 Z"/>
    </g>
    <g class="inner-cut" fill="none" stroke="var(--cut-line)" stroke-width="1">
      <path d="M152 480 V612 H232 L262 557 H384 L414 612 H488 V480"/>
      <path d="M624 480 V612 H702 L732 557 H854 L884 612 H955 V480"/>
    </g>
  </g>

  <!-- Paper bag, flat front -->
  <g class="paper-bag">
    <rect x="605" y="662" width="122" height="245" fill="var(--kraft)"/>
    <rect x="615" y="662" width="26" height="210" fill="var(--mint)"/>
    <rect x="641" y="662" width="26" height="210" fill="var(--butter)"/>
    <rect x="667" y="662" width="26" height="210" fill="var(--mint)"/>
    <rect x="693" y="662" width="26" height="210" fill="var(--teal)"/>
    <path d="M605 662 H727" stroke="var(--kraft-edge)" stroke-width="3"/>
    <circle cx="666" cy="775" r="48" fill="#fff" stroke="var(--teal)" stroke-width="4"/>
    <text class="brand-name" x="666" y="780" font-size="22" text-anchor="middle">Crumvella</text>
    <text class="bag-seal-text" x="666" y="794" text-anchor="middle">BAKED FRESH</text>
    <g class="bag-contact">
      <circle cx="614" cy="884" r="3" fill="var(--teal)"/>
      <text class="bag-contact-text" x="619" y="886">+973 36512248</text>
      <circle cx="670" cy="884" r="3" fill="var(--teal)"/>
      <text class="bag-contact-text" x="675" y="886">@crumvella</text>
      <circle cx="614" cy="897" r="3" fill="var(--teal)"/>
      <text class="bag-contact-text" x="619" y="899">@crumvella</text>
      <circle cx="670" cy="897" r="3" fill="var(--teal)"/>
      <text class="bag-contact-text" x="675" y="899">@crumvella</text>
    </g>
  </g>
  <path d="M697 908 L740 948 H880" fill="none" stroke="var(--leader)"/>
  <text class="caption" x="750" y="946">Brown Paper Bag</text>

  <!-- Sticker -->
  <g class="sticker">
    <circle cx="912" cy="786" r="101" fill="#fff"/>
    <circle cx="912" cy="786" r="96" fill="none" stroke="var(--teal)" stroke-width="9"/>
    <circle cx="912" cy="786" r="82" fill="none" stroke="var(--teal)" stroke-width="1"/>
    <text class="brand-name" x="912" y="796" font-size="46" text-anchor="middle">Crumvella</text>
    <text class="sticker-text" x="912" y="816" text-anchor="middle">BAKED FRESH</text>
    <text class="sticker-text" x="912" y="832" text-anchor="middle">EVERY DAY</text>
  </g>
  <path d="M1018 795 H1065" stroke="var(--leader)"/>
  <text class="caption" x="1045" y="791">Sticker</text>
</svg>
</body>
</html>
```